Outdoor sign for Brindle Auto Restoration

I need a horizontal 4'x 8' outdoor roadside sign for my classic auto restoration business. I have uploaded colors and our logo. Needs the Brindle name, a prominent Classic AUTO RESTORATION, phone number and website. We rebuild and restore vintage cars, trucks and 4x4s. I'd like something clean but possibly retro. Classic Auto Restoration is more important than the Brindle name. It needs to be visible and readable from the street. NO CLIP ART

Target Market(s)

Customers who need their vintage care restored or upgraded. Men and women ages 25-75

Industry/Entity Type

Automotive

Colors
FFC000
F8CF3A
FAE287
FDF2CF
FEFAEE

Requirements
Must have
• Legible. Bright. Readable as a backlit 4' x 8' large horizontal sign (roughly 120cm X 240cm)
Nice to have
• Use of the Brindle logo/type, Complete or Classic before prominent AUTO RESTORATION
Should not have
• Clip art of old cars or icons. And we don't want the Brindle Logo from the website because it wont be legible from the road. I have included the Illustrator file for Brindle text in the uploads

```html
<!DOCTYPE html>
<html lang="en">
<head>
<meta charset="utf-8">
<title>Brindle Auto Restoration – Roadside Sign</title>
<link rel="stylesheet" href="https://fonts.googleapis.com/css2?family=Anton&family=Lobster&family=Roboto+Condensed:wght@700&display=swap">
<style>
  :root {
    --page: #ffffff;
    --sign-border: #ffffff;
    --ink: #161518;
    --amber: #f7a600;
    --wing-tone: #3a2f1a;
    --paper: #ffffff;
  }
  html, body {
    margin: 0;
    width: 1200px;
    height: 1000px;
    overflow: hidden;
    background: var(--page);
  }
  .sign {
    display: block;
    width: 1200px;
    height: 1000px;
  }
  .sign__card { fill: var(--sign-border); }
  .sign__frame { fill: var(--ink); }
  .sign__panel { fill: var(--amber); }
  .wing { fill: var(--wing-tone); opacity: .85; }
  .tagline-classic {
    font-family: "Lobster", cursive;
    font-size: 64px;
    fill: var(--ink);
  }
  .headline {
    font-family: "Anton", sans-serif;
    fill: var(--ink);
  }
  .brand-name {
    font-family: "Roboto Condensed", sans-serif;
    font-weight: 700;
    font-size: 60px;
    fill: var(--amber);
  }
  .contact {
    font-family: "Roboto Condensed", sans-serif;
    font-weight: 700;
    font-size: 60px;
    fill: var(--paper);
  }
  .contact__dot { fill: var(--amber); }
</style>
</head>
<body>
<svg class="sign" viewBox="0 0 1200 1000" xmlns="http://www.w3.org/2000/svg" role="img" aria-label="Brindle Classic Auto Restoration roadside sign">
  <rect class="sign__card" x="83" y="241" width="1035" height="517"/>
  <rect class="sign__frame" x="108" y="267" width="984" height="466"/>
  <polygon class="sign__panel" points="126,284 1074,284 1074,594 600,581 126,594"/>

  <rect class="wing" x="396" y="297" width="98" height="60" rx="6" role="img" aria-label="Winged ornament, left"/>
  <rect class="wing" x="707" y="297" width="98" height="60" rx="6" role="img" aria-label="Winged ornament, right"/>
  <text class="tagline-classic" x="600" y="350" text-anchor="middle" textLength="176" lengthAdjust="spacingAndGlyphs">Classic</text>

  <text class="headline" x="445" y="460" font-size="118" textLength="307" lengthAdjust="spacingAndGlyphs">AUTO</text>
  <text class="headline" x="156" y="578" font-size="134" textLength="888" lengthAdjust="spacingAndGlyphs">RESTORATION</text>

  <text class="brand-name" x="600" y="647" text-anchor="middle" textLength="230" lengthAdjust="spacingAndGlyphs">BRINDLE</text>

  <text class="contact" x="162" y="707" textLength="271" lengthAdjust="spacingAndGlyphs">501-555-0142</text>
  <circle class="contact__dot" cx="485" cy="691" r="9"/>
  <text class="contact" x="535" y="707" textLength="504" lengthAdjust="spacingAndGlyphs">brindle autoworks.com</text>
</svg>
</body>
</html>
```